Korvane Sky Works, LLC - Business Card

I currently have a drone business that specializes in aerial photography, thermal image inspections, deer recovery, search and rescue, custom agricultural applications. i will attach my current business card as well as some logos to incorporate for a new up to date business card
Updates

Designs look the same

Sick

Target Market(s)

farmers, hunters

Contact Information for Business Card

name address phone number (as existing card i attached)

Requirements
Must have
• im good with existing business card, but would like an agricultural twist

```html
<!DOCTYPE html>
<html lang="en">
<head>
<meta charset="utf-8">
<title>Korvane Sky Works, LLC – Business Card</title>
<link rel="stylesheet" href="https://fonts.googleapis.com/css2?family=Source+Sans+3:wght@400;700&display=swap">
<style>
  :root {
    --page-bg: #e4e6e5;
    --card-bg: #f1f1f1;
    --ink: #151515;
    --brand-red: #cc1a21;
    --pill-text: #fbeaea;
    --field-green: #6f8f3a;
    --field-green-dark: #56722b;
    --field-soil: #8a6a3f;
  }
  * { margin: 0; padding: 0; box-sizing: border-box; }
  html, body { width: 1200px; height: 1200px; overflow: hidden; }
  body {
    background: var(--page-bg);
    font-family: "Source Sans 3", Arial, sans-serif;
    color: var(--ink);
    position: relative;
  }
  .card {
    position: absolute;
    left: 236px;
    width: 728px;
    height: 416px;
    background: var(--card-bg);
    border-radius: 3px;
    box-shadow: 0 10px 28px rgba(0,0,0,0.18);
    overflow: hidden;
  }
  .card--front { top: 134px; }
  .card--back { top: 610px; }

  .field-band {
    position: absolute;
    left: 0;
    width: 100%;
    height: 26px;
    display: block;
  }
  .card--front .field-band { bottom: 0; }
  .card--back .field-band { top: 0; }

  .identity {
    position: absolute;
    left: 58px;
    top: 64px;
    display: flex;
    align-items: baseline;
    gap: 14px;
  }
  .identity__name {
    font-weight: 700;
    font-size: 25px;
    letter-spacing: 1.4px;
    word-spacing: 8px;
  }
  .identity__divider { color: var(--brand-red); font-size: 20px; }
  .identity__role { font-size: 20px; }

  .contact-list {
    position: absolute;
    left: 58px;
    top: 196px;
    list-style: none;
    font-size: 19px;
    line-height: 1.3;
  }
  .contact-list li {
    display: flex;
    align-items: flex-start;
    gap: 10px;
    margin-bottom: 5px;
  }
  .contact-list li.contact-list__address { margin-bottom: 14px; }
  .contact-list svg { width: 17px; height: 17px; margin-top: 4px; flex: none; }

  .brand {
    display: flex;
    align-items: center;
    gap: 10px;
    color: var(--brand-red);
    font-weight: 700;
    letter-spacing: 2px;
  }
  .brand__dot {
    border-radius: 50%;
    border: 3px solid var(--brand-red);
  }
  .brand--small {
    position: absolute;
    left: 500px;
    top: 300px;
    font-size: 30px;
  }
  .brand--small .brand__dot { width: 28px; height: 28px; }
  .brand--large {
    position: absolute;
    left: 0;
    right: 0;
    top: 118px;
    justify-content: center;
    font-size: 48px;
  }
  .brand--large .brand__dot { width: 44px; height: 44px; border-width: 4px; }

  .services {
    position: absolute;
    left: 78px;
    top: 242px;
    width: 574px;
    display: grid;
    grid-template-columns: 252px 252px;
    column-gap: 70px;
    row-gap: 13px;
  }
  .services__item {
    height: 31px;
    border-radius: 16px;
    background: var(--brand-red);
    color: var(--pill-text);
    font-size: 18px;
    display: flex;
    align-items: center;
    justify-content: center;
  }
  .services__item--wide {
    grid-column: 1 / span 2;
    justify-self: center;
    width: 300px;
    background: var(--field-green-dark);
  }
</style>
</head>
<body>
  <section class="card card--front" aria-label="Card front">
    <div class="identity">
      <span class="identity__name">DORIAN VESK</span>
      <span class="identity__divider">|</span>
      <span class="identity__role">Owner</span>
    </div>

    <ul class="contact-list">
      <li class="contact-list__address">
        <svg viewBox="0 0 24 24" aria-hidden="true"><path fill="#cc1a21" d="M12 2a7 7 0 0 0-7 7c0 5 7 13 7 13s7-8 7-13a7 7 0 0 0-7-7zm0 9.5A2.5 2.5 0 1 1 12 6.5a2.5 2.5 0 0 1 0 5z"/></svg>
        <span>214 W. Orchard Rd. Hallow,<br>OH 45900</span>
      </li>
      <li>
        <svg viewBox="0 0 24 24" aria-hidden="true"><path fill="#cc1a21" d="M6.6 10.8a15 15 0 0 0 6.6 6.6l2.2-2.2c.3-.3.7-.4 1-.2 1.1.4 2.3.6 3.6.6.6 0 1 .4 1 1V20c0 .6-.4 1-1 1A17 17 0 0 1 3 4c0-.6.4-1 1-1h3.5c.6 0 1 .4 1 1 0 1.3.2 2.5.6 3.6.1.3 0 .7-.2 1z"/></svg>
        <span>419-555-0186</span>
      </li>
      <li>
        <svg viewBox="0 0 24 24" aria-hidden="true"><rect x="2.5" y="5" width="19" height="14" fill="none" stroke="#cc1a21" stroke-width="1.8"/><path d="M3 6l9 7 9-7" fill="none" stroke="#cc1a21" stroke-width="1.8"/></svg>
        <span>korvaneskyworks@mail.com</span>
      </li>
      <li>
        <svg viewBox="0 0 24 24" aria-hidden="true"><g fill="none" stroke="#cc1a21" stroke-width="1.6"><circle cx="12" cy="12" r="9.5"/><ellipse cx="12" cy="12" rx="4.2" ry="9.5"/><path d="M2.5 12h19M4 7h16M4 17h16"/></g></svg>
        <span>www.korvaneskyworks.com</span>
      </li>
    </ul>

    <div class="brand brand--small">
      <span class="brand__dot"></span>
      <span class="brand__name">KORVANE</span>
    </div>

    <svg class="field-band" viewBox="0 0 728 26" preserveAspectRatio="none" aria-hidden="true">
      <rect width="728" height="26" fill="var(--field-green)"/>
      <rect y="0" width="728" height="4" fill="var(--field-soil)"/>
      <g stroke="var(--field-green-dark)" stroke-width="2">
        <line x1="0" y1="11" x2="728" y2="11"/>
        <line x1="0" y1="18" x2="728" y2="18"/>
      </g>
    </svg>
  </section>

  <section class="card card--back" aria-label="Card back">
    <svg class="field-band" viewBox="0 0 728 26" preserveAspectRatio="none" aria-hidden="true">
      <rect width="728" height="26" fill="var(--field-green)"/>
      <rect y="22" width="728" height="4" fill="var(--field-soil)"/>
      <g stroke="var(--field-green-dark)" stroke-width="2">
        <line x1="0" y1="8" x2="728" y2="8"/>
        <line x1="0" y1="15" x2="728" y2="15"/>
      </g>
    </svg>

    <div class="brand brand--large">
      <span class="brand__dot"></span>
      <span class="brand__name">KORVANE</span>
    </div>

    <div class="services">
      <span class="services__item">Thermal Image Inspections</span>
      <span class="services__item">Real Estate Photography</span>
      <span class="services__item">Search &amp; Rescue</span>
      <span class="services__item">Deer Recovery</span>
      <span class="services__item services__item--wide">Custom Agricultural Applications</span>
    </div>
  </section>
</body>
</html>
```